Private Bar sign _ Vinyl over Perplex - Tam's Bar

We have a light box (illuminated) and need a design for it. The finished size is 1270mm wide and 270mm high.

The backgound colour is supposed to be tomato red (when lit!) so I guess the unlit colour would need to be a lot darker.

We want to have:
2 Kordvale Bottles with the cap popping and beer squirting out
The sign to say "Tam's Bar" with a sub-line "What happens in the bar stays in the bar"

We have a 70's Juke box and it we would love it to have a bit of that theme. Not silly but rather smashing! A bit of a 3-D Look would be a real bonus. I have attached an image of what someone did for us and we hate it. They have not even cut it in nicely and applied it while we were out. Have a look at the bar and I bet you can come up with a much better sign.
Updates

Font styles to use
Script

Colors
ec1f27

Requirements
Must have
• Tomato red when illuminated
• 70's or 80's look
• 2 Kordvale Bottles with the cap popping and beer and foam squirting out
• The sign to say "Tam's Bar" with a sub-line "What happens in the bar stays in the bar"
• Even a Pin up girl in there would not hurt!
• The writing Tam's bar should look like hand writing
• Be creative :-)
Nice to have
• A 3-D look would be awesome!
• Bold and strong colours
Should not have
• The attached sample is how we do NOT like it to look like. It is sterile. The red turns into bright orange when illuminated ( we hate orange!)

```html
<!DOCTYPE html>
<html lang="en">
<head>
<meta charset="utf-8">
<title>Tam's Bar – Light Box Sign</title>
<link rel="stylesheet" href="https://fonts.googleapis.com/css2?family=Kaushan+Script&family=Caveat+Brush&display=swap">
<style>
  :root {
    --sign-red: #6a0509;
    --neon-core: #cfe9ff;
    --neon-tube: #3f8cff;
    --neon-glow: #1e5dff;
    --tagline-white: #ffffff;
    --bottle-green: #2c7a2a;
    --bottle-dark: #1b4d18;
    --splash-light: #c9b7a4;
  }
  html, body {
    margin: 0;
    padding: 0;
    overflow: hidden;
    background: var(--sign-red);
  }
  .sign {
    position: relative;
    width: 1200px;
    height: 255px;
    background: var(--sign-red);
    overflow: hidden;
  }
  .bottle-art {
    position: absolute;
    top: 4px;
    width: 236px;
    height: 232px;
  }
  .bottle-art--left { left: 2px; }
  .bottle-art--right { right: 2px; }
  .bar-name {
    position: absolute;
    left: 240px;
    top: 0;
    width: 640px;
    height: 200px;
    overflow: visible;
  }
  .bar-name text {
    font-family: "Kaushan Script", cursive;
    font-size: 124px;
  }
  .tagline {
    position: absolute;
    left: 280px;
    top: 190px;
    width: 570px;
    margin: 0;
    text-align: center;
    font-family: "Caveat Brush", cursive;
    font-size: 36px;
    line-height: 1;
    color: var(--tagline-white);
    white-space: nowrap;
  }
</style>
</head>
<body>
<main class="sign">
  <svg class="bottle-art bottle-art--left" viewBox="0 0 236 232" role="img" aria-label="Kordvale beer bottle with cap popping and beer and foam splashing out">
    <defs>
      <radialGradient id="bottleAreaLeft" cx="0.5" cy="0.5" r="0.6">
        <stop offset="0" stop-color="var(--bottle-green)" stop-opacity="0.55"/>
        <stop offset="0.6" stop-color="var(--splash-light)" stop-opacity="0.18"/>
        <stop offset="1" stop-color="var(--sign-red)" stop-opacity="0"/>
      </radialGradient>
    </defs>
    <rect width="236" height="232" rx="24" fill="url(#bottleAreaLeft)"/>
  </svg>

  <svg class="bar-name" viewBox="0 0 640 200">
    <defs>
      <filter id="neonGlow" x="-30%" y="-40%" width="160%" height="180%">
        <feGaussianBlur stdDeviation="7"/>
      </filter>
    </defs>
    <g text-anchor="middle">
      <text x="322" y="155" fill="none" stroke="var(--neon-glow)" stroke-width="14" filter="url(#neonGlow)" aria-hidden="true">Tam's Bar</text>
      <text x="322" y="155" fill="none" stroke="var(--neon-tube)" stroke-width="6">Tam's Bar</text>
      <text x="322" y="155" fill="none" stroke="var(--neon-core)" stroke-width="1.6" aria-hidden="true">Tam's Bar</text>
    </g>
  </svg>

  <p class="tagline">What happens in the bar stays in the bar</p>

  <svg class="bottle-art bottle-art--right" viewBox="0 0 236 232" role="img" aria-label="Kordvale beer bottle with cap popping and beer and foam splashing out">
    <defs>
      <radialGradient id="bottleAreaRight" cx="0.5" cy="0.5" r="0.6">
        <stop offset="0" stop-color="var(--bottle-green)" stop-opacity="0.55"/>
        <stop offset="0.6" stop-color="var(--splash-light)" stop-opacity="0.18"/>
        <stop offset="1" stop-color="var(--sign-red)" stop-opacity="0"/>
      </radialGradient>
    </defs>
    <rect width="236" height="232" rx="24" fill="url(#bottleAreaRight)"/>
  </svg>
</main>
</body>
</html>
```